Packaging Design for Face Mask Box

We are looking for an attractive but subtle packaging design for Face Masks (for non medical use). 50pcs per box.

The brand name should be "Kelvano". We have not yet got a logo or a text selected (font) for the brand name so we are open to your ideas on how "Kelvano" could look. It could have some elements of fresh air or breathing etc so symbolize clean and healthier air or something along those lines.

The box dimensions should be 180mm (L) x 100mm (W) x 90mm (H).

The box should have a perforation on top - exactly similar to Tissue Box packs. So, in order to access the face masks, the user should tear off the perforation and extract one mask at a time.

As this is not a medical grade face mask, the product should indicate "For Non- Medical Use". Also the heading of the masks should be DISPOSABLE PROTECTIVE FACE MASKS with sub heading 3 PLY FACE MASKS WITH EAR LOOP.

We will also prefer to have the Instructions to use and Precautions which are commonly available on face mask packages. This could be printed either on the sides or on the bottom of the package. There should also be a blank space on one of the sides to print Batch No. Mfg Date and Exp Date.

The box design could have some design resemblance to our company logo which is hereby attached in high resolution. However this is not compulsory.

The following phrases could be mentioned on the box to highlight some of the product features:

Dual Charge Electrostatic fibres for extra filtration
Improved Nose Bridge Strips for better protection
Tri-layer barrier with 3 x 25 g/m2 material
In-house production of filter material for Quality Consistency

I have added 3 samples face mask box designs from other manufacturers for your reference to get an idea of the box shape etc.

If you have any more questions, please feel free to ask.

Good luck!

```html
<!DOCTYPE html>
<html lang="en">
<head>
<meta charset="utf-8">
<title>Kelvano Disposable Protective Masks – Box Net</title>
<link href="https://fonts.googleapis.com/css2?family=Exo+2:wght@500;700;800&family=Open+Sans:wght@400;600&display=swap" rel="stylesheet">
<style>
  :root{
    --stage:#e6e8ea;
    --sky-light:#d3e4f1;
    --sky:#b9d3e8;
    --navy:#143a60;
    --navy-deep:#0f2f50;
    --ocean:#1e5b93;
    --accent:#3d8fcf;
    --white:#ffffff;
    --ink-soft:#2f5576;
  }
  *{box-sizing:border-box;margin:0;padding:0}
  html,body{width:1200px;height:666px;overflow:hidden}
  body{background:var(--stage);font-family:"Open Sans",sans-serif;position:relative}

  .panel{position:absolute;overflow:hidden}
  .panel svg.backdrop{position:absolute;inset:0;width:100%;height:100%}

  /* top panel */
  .panel--top{left:124px;top:10px;width:612px;height:340px;background:linear-gradient(160deg,var(--sky-light),var(--sky))}
  .perforation{position:absolute;left:186px;top:150px;width:240px;height:46px;border-radius:50%;background:var(--white);border:2px dashed var(--ocean)}
  .count-badge{position:absolute;left:560px;top:18px;width:34px;height:48px;background:var(--navy);color:var(--white);font-family:"Exo 2",sans-serif;font-weight:800;font-size:17px;display:flex;flex-direction:column;align-items:center;justify-content:center;line-height:1;transform:rotate(180deg)}
  .count-badge small{font-size:7px;font-weight:500;margin-top:2px}
  .top-brand{position:absolute;left:352px;top:230px;font-family:"Exo 2",sans-serif;font-weight:800;font-size:40px;letter-spacing:2px;color:var(--white);transform:rotate(180deg)}

  /* front panel */
  .panel--front{left:124px;top:350px;width:612px;height:306px;background:linear-gradient(120deg,var(--sky-light),var(--sky));border-top:1px solid rgba(20,58,96,.15)}
  .brand{position:absolute;left:30px;top:22px;font-family:"Exo 2",sans-serif;font-weight:800;font-size:42px;letter-spacing:1.5px;color:var(--navy)}
  .features{position:absolute;left:32px;top:80px;list-style:none;font-size:7.5px;color:var(--ink-soft);line-height:1.75}
  .features li::before{content:"•";margin-right:4px;color:var(--accent)}
  .mask-visual{position:absolute;left:250px;top:88px;width:210px;height:124px;border-radius:18px 18px 30px 30px;background:linear-gradient(180deg,#d9e9f6,#9fc3e2)}
  .title{position:absolute;left:32px;top:188px;font-family:"Exo 2",sans-serif;line-height:1}
  .title__main{display:block;font-weight:700;font-size:36px;letter-spacing:1px;color:var(--accent)}
  .title__sub{display:block;font-weight:500;font-size:21px;letter-spacing:.5px;color:var(--navy);margin-top:4px}
  .divider{position:absolute;left:262px;top:222px;width:2px;height:42px;background:var(--navy)}
  .spec{position:absolute;left:274px;top:226px;font-family:"Exo 2",sans-serif;color:var(--navy);font-size:11px;letter-spacing:1px;line-height:1.4}
  .spec b{font-weight:500;font-size:12px;letter-spacing:.3px;display:block}

  /* side panel */
  .panel--side{left:736px;top:350px;width:340px;height:306px;background:var(--navy);border-left:1px solid rgba(255,255,255,.2)}
  .howto-title{position:absolute;left:160px;top:28px;font-size:7.5px;font-weight:600;letter-spacing:1px;color:var(--white);text-transform:uppercase}
  .step{position:absolute;width:150px;display:flex;flex-direction:column;align-items:center;gap:6px}
  .step__figure{width:58px;height:58px;border-radius:50%;background:radial-gradient(circle at 50% 40%,#f0b48e,#e05a3c 70%)}
  .step__text{font-size:7px;color:var(--white);text-align:center;line-height:1.4}
</style>
</head>
<body>

<section class="panel panel--top" aria-label="Top panel">
  <svg class="backdrop" viewBox="0 0 612 340" preserveAspectRatio="none" aria-hidden="true">
    <path d="M612 40 C470 60 420 150 440 220 C455 275 420 320 360 340 L612 340 Z" fill="var(--ocean)" opacity=".55"/>
    <path d="M612 70 C500 90 455 160 470 225 C483 280 450 320 400 340 L612 340 Z" fill="var(--navy)"/>
  </svg>
  <div class="count-badge">50<small>PCS</small></div>
  <div class="perforation" aria-label="Tear-off perforation"></div>
  <div class="top-brand">KELVANO</div>
</section>

<section class="panel panel--front" aria-label="Front panel">
  <svg class="backdrop" viewBox="0 0 612 306" preserveAspectRatio="none" aria-hidden="true">
    <path d="M612 0 L470 0 C560 60 540 150 470 215 C420 260 430 290 460 306 L612 306 Z" fill="var(--ocean)" opacity=".45"/>
    <path d="M612 0 L520 0 C590 70 580 160 515 220 C475 258 480 290 505 306 L612 306 Z" fill="var(--navy)"/>
  </svg>
  <h1 class="brand">KELVANO</h1>
  <ul class="features">
    <li>Dual Charge Electrostatic fibres for extra filtration</li>
    <li>Improved Nose Bridge Strips for better protection</li>
    <li>Tri-layer barrier with 3 x 25 g/m² material</li>
    <li>In-house production of filter material for Quality Consistency</li>
  </ul>
  <div class="mask-visual" role="img" aria-label="Image of a pleated light blue 3-ply face mask with white ear loop"></div>
  <h2 class="title">
    <span class="title__main">DISPOSABLE</span>
    <span class="title__sub">PROTECTIVE MASKS</span>
  </h2>
  <div class="divider"></div>
  <p class="spec">3 PLY WITH EAR LOOP<b>For Non- Medical Use</b></p>
</section>

<section class="panel panel--side" aria-label="Side panel with instructions">
  <svg class="backdrop" viewBox="0 0 340 306" preserveAspectRatio="none" aria-hidden="true">
    <path d="M0 0 L70 0 C20 70 25 170 60 230 C80 265 70 290 50 306 L0 306 Z" fill="var(--ocean)"/>
    <path d="M0 0 L40 0 C0 70 5 170 30 230 C45 265 40 290 25 306 L0 306 Z" fill="var(--navy-deep)"/>
  </svg>
  <p class="howto-title">How to wear</p>
  <div class="step" style="left:180px;top:46px">
    <div class="step__figure" role="img" aria-label="Illustration of a person washing hands"></div>
    <p class="step__text">Wash hands before touching the mask.</p>
  </div>
  <div class="step" style="left:60px;top:84px">
    <div class="step__figure" role="img" aria-label="Illustration of a person holding the mask by its ear loops"></div>
    <p class="step__text">Hold by ear loops, blue side out.</p>
  </div>
  <div class="step" style="left:180px;top:164px">
    <div class="step__figure" role="img" aria-label="Illustration of a person pressing the nose strip"></div>
    <p class="step__text">Press nose strip to fit your face.</p>
  </div>
  <div class="step" style="left:60px;top:196px">
    <div class="step__figure" role="img" aria-label="Illustration of a person discarding a used mask"></div>
    <p class="step__text">Discard after use; do not reuse.</p>
  </div>
</section>

</body>
</html>
```